依頼詳細
【仕様】
『資格完全攻略 突破 ケアワーカー ノート&ドリル 2014 基礎分野編』『資格完全攻略 突破 ケアワーカー ノート&ドリル 2014 応用分野編』は同じ仕様となります。
・B5(182 × 257 ㎜)
・背幅はおよそ20㎜です(修正有)。
・本文は横書ですので左綴じとなります。
・カバー(表1、表4、背表紙):4C(フルカラー)
・表紙(表1、表4、背表紙):1C
・扉:1C

※表紙・扉のデザインはカバーデザインに基づいたもので、「書名」「編者名」「社名」だけが入っているもので結構です。
記載項目
【デザインについて】
・同資格のための参考書・問題集・ワークブックは類書が数多くあり、なかなか差別化が図れないのが現状です。今回は、「資格受験用テキスト・問題集」によく見られるようなキャッチコピーが踊るデザインではなく、すっきりとした知的かつスマートなデザインを希望します。
・書籍の内容は堅いですが、読者が手に取りやすい親しみやすさも加味してください。
・『要点整理と演習集』のデザインにはとらわれませんし、イラスト等を加えていただいても結構です。
・タイトルの文字についてですが、「ケアワーカー」「突破」「2014」「共通科目編」「応用分野編」が目に付くようにしてください。特に「ケアワーカー」の文言については100級以上の大きさでお願いをします。
・2つの書籍でデザインに盛り込む内容(文字)が異なります。書名、編者名等のデザインに盛り込む内容(文字)は添付ファイルを参照してください。

その他、ご不明な点は、お気軽にお問い合わせください。
希望イメージ
シンプル 複雑
単色 カラフル
暗い 明るい
日常 高級
遊び心 厳粛
未来的 伝統的
女性的 男性的
希望する色
特になし
納品ファイル
• イラストレーター形式 (.ai)
補足説明
■ 選んだ理由

①従来の弊社の書籍とは違うやわらかいイメージ。
②他社の類書との差別化がはかれるデザイン。
③書籍の内容(テキスト・問題集)がもつ「堅い」イメージをやわらげてくれるデザイン。

■ 提案者全員のお礼・コメント

この度は多くのご提案ありがとうございました。
ご応募くださった皆様の提案はとてもバラエティに富み、素晴らしいものが多く迷いましたが、上記の理由により選定させていただきました。
それぞれの提案に社内では「他の書籍ならこのデザインがいい」といった声もきかれました。今回の書籍では惜しくも採用にいたらなかった提案も違う案件によっては十分に採用される可能性がありました。
今後もこのようなデザインをしていただきたい案件がございます。またの機会にも是非ご応募くださいますようお願いいたします。

```html
<!DOCTYPE html>
<html lang="ja">
<head>
<meta charset="utf-8">
<title>資格完全攻略 突破 ケアワーカー ノート&amp;ドリル 2014 応用分野編</title>
<link rel="stylesheet" href="https://fonts.googleapis.com/css2?family=Noto+Sans+JP:wght@400;500;700;900&display=swap">
<style>
  :root {
    --paper: #ffffff;
    --ink: #2b2b22;
    --orange: #f08c1e;
    --lime: #a9c431;
    --lime-dark: #7f9a1a;
    --soft: #f4f7e4;
  }
  html, body { margin: 0; padding: 0; overflow: hidden; }
  body { width: 848px; height: 1200px; background: var(--paper); font-family: "Noto Sans JP", sans-serif; color: var(--ink); }
  .cover { position: relative; width: 848px; height: 1200px; overflow: hidden; background: var(--paper); }

  .series-tag { position: absolute; right: 0; top: 0; width: 160px; height: 150px; background: var(--orange); color: #fff; box-sizing: border-box; padding: 22px 14px 0 0; text-align: right; }
  .series-tag .series { font-size: 23px; font-weight: 700; letter-spacing: 1px; display: block; white-space: nowrap; }
  .series-tag .goal { font-size: 52px; font-weight: 900; line-height: 1.2; display: block; }

  .edition { position: absolute; left: 85px; top: 62px; width: 295px; height: 178px; border: 4px solid var(--lime); box-sizing: border-box; text-align: center; }
  .edition .year { display: block; font-size: 40px; font-weight: 700; color: var(--lime-dark); margin-top: 16px; letter-spacing: 2px; }
  .edition .part { display: block; font-size: 52px; font-weight: 900; color: var(--lime-dark); line-height: 1.3; }

  .subjects { position: absolute; left: 60px; top: 335px; width: 372px; margin: 0; padding: 0; list-style: none; }
  .subjects li { font-size: 15.5px; font-weight: 700; height: 48px; line-height: 48px; margin-bottom: 12px; padding-left: 14px; white-space: nowrap; border-left: 8px solid var(--lime); border-bottom: 2px solid var(--lime); background: var(--soft); }

  .title { position: absolute; left: 590px; top: 160px; margin: 0; writing-mode: vertical-rl; font-size: 112px; font-weight: 900; letter-spacing: 2px; line-height: 1; color: var(--ink); white-space: nowrap; }
  .subtitle { position: absolute; left: 490px; top: 250px; writing-mode: vertical-rl; font-size: 50px; font-weight: 900; color: var(--orange); line-height: 1; letter-spacing: 10px; white-space: nowrap; }

  .catch { position: absolute; left: 60px; top: 872px; margin: 0; font-size: 25px; font-weight: 700; line-height: 1.5; white-space: nowrap; }
  .notes { position: absolute; left: 60px; top: 960px; width: 620px; font-size: 13px; line-height: 1.8; }
  .notes p { margin: 0; white-space: nowrap; }
  .notes .label { display: inline-block; color: #fff; font-weight: 700; font-size: 11px; line-height: 1.6; padding: 0 5px; margin-right: 6px; }
  .notes .label.note { background: var(--orange); }
  .notes .label.drill { background: var(--lime-dark); }

  .credits { position: absolute; right: 40px; top: 790px; writing-mode: vertical-rl; font-size: 22px; font-weight: 500; line-height: 1.6; white-space: nowrap; }
  .credits span { display: block; }
  .credits .role { display: inline; margin-top: 0.5em; }

  .publisher { position: absolute; left: 0; width: 848px; top: 1115px; text-align: center; font-size: 26px; font-weight: 700; letter-spacing: 3px; }
</style>
</head>
<body>
<main class="cover">
  <div class="series-tag">
    <span class="series">資格完全攻略</span>
    <span class="goal">突破</span>
  </div>

  <div class="edition">
    <span class="year">2014</span>
    <span class="part">応用分野編</span>
  </div>

  <ul class="subjects">
    <li>社会調査の基礎</li>
    <li>相談援助の基盤と専門職</li>
    <li>相談援助の理論と方法</li>
    <li>福祉サービスの組織と経営</li>
    <li>高齢者に対する支援と介護保険制度</li>
    <li>児童や家庭に対する支援と児童・家庭福祉制度</li>
    <li>就労支援サービス</li>
    <li>更生保護制度</li>
  </ul>

  <h1 class="title">ケアワーカー</h1>
  <div class="subtitle">ノート&amp;ドリル</div>

  <p class="catch">系統立てた記述で理解度アップ！<br>効果的な学習をサポートする合格力養成テキスト</p>

  <div class="notes">
    <p><span class="label note">ノート</span>出題範囲を網羅し、重要な事項を見やすく整理して解説しています。</p>
    <p><span class="label drill">ドリル</span>要点の確認と実力の定着に役立つ演習問題を各章末に収録しています。</p>
  </div>

  <div class="credits">
    <span>森川 涼 <span class="role">監修</span></span>
    <span>ケアワーカー資格研究会 編集</span>
  </div>

  <div class="publisher">株式会社 あさひ書房</div>
</main>
</body>
</html>
```